Help develop the "Breezy Brew" Logo & Can Design for new beer!

We're a new beer being produced in the Caribbean. Thus looking for a beer logo design that
1) capitalizes on the word "Breezy" for further beer lines that spin off of this first one. EXAMPLES OF OTHER BEER NAMES TO BE PRODUCED THAT HAVE TO HAVE TIE IN TO ORIGINAL DESIGN: "One Breezy Brew", "Sunny Pelican Wobble Brew" "Ramblefoot Breezy Brew" "Wharrya doin' Breezy Brew" "Bout now for Breezy Brew", "Tamarna Breezy Brew" etc etc etc,

2) has unique visual impact,
3) Logo has to be usable across variety of mediums,
4) 4 color maximum,
5) Island art feel,
6) Breezy Brew needs to convey a since of "lightness and slight tongue-in-cheek or off beat humor"...but not overwhelming,
7) Each subsequent label names (see above) needs to be distinctly color coded, but connects to the overarching theme of the brand with distinctive interpretations of each beer’s name.
8) Needs to be BOLD in statement and color.

You can get inspiration from some of these logo's. Follow this link: http://www.quorvelstudio.com/vintage-logos/
or http://www.tindralcrate.com/2014/12/30-beers-for-30-years-2001-to-2006.html

Also see attached files for inspiration!!!

Reason: We've extended the deadline for this project! Thus submit any new designs sooner than later. Thanks!

Target Market(s)

Male: Wear jeans & baseball cap, Played H.S. sports, Hunts/fish/golfDrive a truck or SUV, Work a blue collar job, Like working in the garage or on the landLike football/basketball/baseball, Are married high school sweetheart and have childrenAre from southern states...or wished they were, Chews tobacco or smokeDrink beerFemale: Attended college/community collegeAre married with kidsRide motorcycles, 4x4, ATV’sDrive Trucks or vansFish/camp/garden/sewDo craftsDrink beerGets manicures/pedicuresWears jewelry & jeans

Logo Text

Breezy Brew

Logo styles of interest
Emblem Logo
Pictorial/Combination Logo
Abstract Logo
Character Logo
Wordmark Logo
Requirements
Must have
• Eye catching & readable shelf presentation. Non-Standard art. High definition. Bold Statement. Clear design elements, various color options, High color contrast (like attached files) are needed for visual impact. Simple elements that conveys essence of the brand.
• You are designing the whole "beer can" logo elements, not just the the main logo. Things like background and side panels. Back panel for ingredients and messages to be added to. This is an "overall" can design, not just a single logo design.
• MUST HAVE THESE WORDS/SENTENCES/SECTIONS:
• Sentences: Our Breezy ales and lagers are handcrafted with some of the best ingredients the Caribbean has to offer!
• Section: So, Why Do we use can's?
• Can's eliminate potential light damage, reduce the risk of oxidation are lighter and chill quicker. Can be enjoyed on beaches and make for great recycling and table art. Plus they are the most recycled and eco-friendly material we can use. Breezy!
• BREWED AND BOTTLED/PACKED BY:
• IMPORTED BY
• ALCOHOL (ALC) ______% BY VOLUME (VOL)
• Recyclable
• GOVERNMENT WARNING:
• (1) According to the Surgeon General, women should not drink alcoholic beverages during pregnancy because of the risk of birth defects. (2) Consumption of
• alcoholic beverages impairs your ability to drive a car or operate machinery, and may cause health problems.
• Description: (This will change from beer to beer but this is good example of type language we would be using. "This Breezy Brew has a pletheria of Island goodness (there are hints of passion fruit, mango, and pineapple) along with some pleasant bitterness IPAs are known for. We can honestly say these sweet and savory flavors pair perfectly with this beer and you'll get a kick out of the IPA notes too!"
Should not have
• nudity, graphic language, skulls, flames,

```html
<!DOCTYPE html>
<html lang="en">
<head>
<meta charset="utf-8">
<title>Breezy Brew – Logo &amp; Can Design</title>
<link rel="stylesheet" href="https://fonts.googleapis.com/css2?family=Archivo:wght@400;700;800;900&display=swap">
<style>
:root{
  --ink:#141414;
  --maroon:#7a2c30;
  --maroon-deep:#5e1d22;
  --maroon-soft:#a5585b;
  --silver:#e9e9ea;
  --silver-dark:#c4c5c8;
  --orange:#c9782f;
  --orange-deep:#a85a1c;
  --band:#1d1d1d;
  --stage-top:#f6f6f6;
  --stage-bottom:#d9d9db;
  --white:#ffffff;
}
*{box-sizing:border-box;margin:0;padding:0}
html,body{width:1200px;height:2972px;overflow:hidden;background:var(--white)}
body{position:relative;font-family:"Archivo",Arial,sans-serif;color:var(--ink)}
.section{position:absolute;left:0;width:1200px;overflow:hidden}

/* wordmark */
.wordmark{display:flex;flex-direction:column;align-items:center;text-align:center}
.wordmark-dot{width:0.42em;height:0.42em;border-radius:50%;background:currentColor;margin-bottom:0.12em}
.wordmark-name{font-weight:900;text-transform:uppercase;line-height:0.92;letter-spacing:0}
.wordmark-tag{font-weight:800;text-transform:uppercase;letter-spacing:0.12em;font-size:0.2em;margin-top:0.35em;white-space:nowrap}

.logo-section{top:0;height:858px;background:var(--white)}
.logo-section .wordmark{position:absolute;left:0;right:0;top:190px;color:var(--ink);font-size:150px}

.stage{background:linear-gradient(180deg,var(--stage-top),var(--stage-bottom))}
.stage-silver{top:866px;height:661px}
.stage-color{top:1750px;height:633px}
.band{top:1534px;height:216px;background:var(--band)}
.band .wordmark{position:absolute;left:0;right:0;top:46px;color:var(--white);font-size:58px}

/* flat cans */
.can{position:absolute;border-radius:22px;overflow:hidden;background:var(--silver)}
.can-lid{position:absolute;left:0;right:0;top:0;height:20px;background:var(--silver-dark)}
.can-base{position:absolute;left:0;right:0;bottom:0;height:16px;background:var(--silver-dark)}
.can-pattern{position:absolute;left:0;right:0;background:linear-gradient(180deg,var(--maroon),var(--maroon-soft))}
.can-pattern.top{top:20px;height:58px}
.can-pattern.bottom{bottom:16px;height:110px;background:linear-gradient(0deg,var(--maroon),var(--maroon-soft))}
.can .wordmark{position:absolute;left:0;right:0;top:150px;color:var(--maroon);font-size:42px}
.can-main{left:491px;width:218px}
.can-side{width:184px}
.can-left{left:282px}
.can-right{left:734px}
.stage-silver .can-main{top:54px;height:564px}
.stage-silver .can-side{top:98px;height:487px}
.stage-color .can-main{top:50px;height:534px}
.stage-color .can-side{top:92px;height:452px}
.stage-color .can-side .wordmark{top:120px;font-size:34px}
.can-orange{background:var(--orange)}
.can-orange .wordmark{color:var(--maroon-deep)}
.can-orange .can-pattern{background:linear-gradient(180deg,var(--orange-deep),var(--orange))}
.can-maroon{background:var(--maroon)}
.can-maroon .wordmark{color:var(--white)}
.can-maroon .can-pattern{background:linear-gradient(180deg,var(--maroon-deep),var(--maroon-soft))}
.can-copy{position:absolute;left:18px;right:14px;top:120px;font-size:15px;line-height:1.35;font-weight:800;color:var(--ink)}
.can-copy.small{font-weight:400;font-size:11px}

/* flat label */
.label{top:2383px;height:589px;background:var(--white)}
.label-pattern{position:absolute;left:0;right:0;background:linear-gradient(180deg,var(--maroon),var(--maroon-soft))}
.label-pattern.top{top:0;height:90px}
.label-pattern.bottom{bottom:0;height:125px;background:linear-gradient(0deg,var(--maroon),var(--maroon-soft))}
.warning{position:absolute;left:12px;top:110px;width:86px;height:290px}
.warning p{position:absolute;left:0;top:0;width:290px;height:86px;transform-origin:0 0;transform:translate(0,290px) rotate(-90deg);font-size:10px;line-height:1.22}
.warning strong{font-weight:800}
.label-intro{position:absolute;left:118px;top:130px;width:280px;font-size:23px;line-height:1.3;font-weight:800;text-align:justify}
.label-packer{position:absolute;left:118px;top:405px;width:280px;font-size:10px;line-height:1.35;font-weight:700;text-transform:uppercase;display:flex;gap:8px}
.label-packer .mark{flex:none;width:16px;height:16px;border-radius:50%;background:var(--ink)}
.label .wordmark{position:absolute;left:430px;width:340px;top:140px;color:var(--maroon);font-size:74px}
.label-cans{position:absolute;left:915px;top:125px;width:265px}
.label-cans h2{font-size:14px;font-weight:800;text-transform:uppercase;margin-bottom:10px}
.label-cans p{font-size:14px;line-height:1.38;font-weight:700;text-align:justify}
.label-alc{position:absolute;left:930px;top:405px;font-size:9.5px;font-weight:700;line-height:1.4;text-transform:uppercase}
.label-alc span{text-transform:none;display:block}
</style>
</head>
<body>

<section class="section logo-section">
  <div class="wordmark"><span class="wordmark-dot"></span><span class="wordmark-name">Breezy<br>Brew</span><span class="wordmark-tag">Caribbean Beer</span></div>
</section>

<section class="section stage stage-silver">
  <div class="can can-side can-left">
    <div class="can-lid"></div>
    <div class="can-pattern top" role="img" aria-label="Maroon paisley wave ornament"></div>
    <p class="can-copy">Our Breezy ales and lagers are handcrafted with some of the best ingredients the Caribbean has to offer!</p>
    <div class="can-pattern bottom" role="img" aria-label="Maroon paisley wave ornament"></div>
    <div class="can-base"></div>
  </div>
  <div class="can can-main">
    <div class="can-lid"></div>
    <div class="can-pattern top" role="img" aria-label="Maroon paisley wave ornament"></div>
    <div class="wordmark"><span class="wordmark-dot"></span><span class="wordmark-name">Breezy<br>Brew</span><span class="wordmark-tag">Caribbean Beer</span></div>
    <div class="can-pattern bottom" role="img" aria-label="Maroon paisley wave ornament"></div>
    <div class="can-base"></div>
  </div>
  <div class="can can-side can-right">
    <div class="can-lid"></div>
    <div class="can-pattern top" role="img" aria-label="Maroon paisley wave ornament"></div>
    <p class="can-copy small">So, why do we use can's? Can's eliminate potential light damage, reduce the risk of oxidation are lighter and chill quicker. Can be enjoyed on beaches and make for great recycling and table art.</p>
    <div class="can-pattern bottom" role="img" aria-label="Maroon paisley wave ornament"></div>
    <div class="can-base"></div>
  </div>
</section>

<section class="section band">
  <div class="wordmark"><span class="wordmark-dot"></span><span class="wordmark-name">Breezy<br>Brew</span><span class="wordmark-tag">Caribbean Beer</span></div>
</section>

<section class="section stage stage-color">
  <div class="can can-side can-left can-orange">
    <div class="can-lid"></div>
    <div class="wordmark"><span class="wordmark-dot"></span><span class="wordmark-name">Breezy<br>Brew</span><span class="wordmark-tag">Caribbean Beer</span></div>
    <div class="can-pattern bottom" role="img" aria-label="Amber paisley wave ornament"></div>
    <div class="can-base"></div>
  </div>
  <div class="can can-main">
    <div class="can-lid"></div>
    <div class="can-pattern top" role="img" aria-label="Maroon paisley wave ornament"></div>
    <div class="wordmark"><span class="wordmark-dot"></span><span class="wordmark-name">Breezy<br>Brew</span><span class="wordmark-tag">Caribbean Beer</span></div>
    <div class="can-pattern bottom" role="img" aria-label="Maroon paisley wave ornament"></div>
    <div class="can-base"></div>
  </div>
  <div class="can can-side can-right can-maroon">
    <div class="can-lid"></div>
    <div class="wordmark"><span class="wordmark-dot"></span><span class="wordmark-name">Breezy<br>Brew</span><span class="wordmark-tag">Caribbean Beer</span></div>
    <div class="can-pattern bottom" role="img" aria-label="Dark red paisley wave ornament"></div>
    <div class="can-base"></div>
  </div>
</section>

<section class="section label">
  <div class="label-pattern top" role="img" aria-label="Maroon paisley wave ornament border"></div>
  <div class="warning"><p><strong>GOVERNMENT WARNING:</strong> (1) According to the Surgeon General, women should not drink alcoholic beverages during pregnancy because of the risk of birth defects. (2) Consumption of alcoholic beverages impairs your ability to drive a car or operate machinery, and may cause health problems.</p></div>
  <p class="label-intro">Our Breezy ales and lagers are handcrafted with some of the best ingredients the Caribbean has to offer!</p>
  <div class="label-packer"><span class="mark"></span><span>Brewed and bottled/packed by:<br>Imported by</span></div>
  <div class="wordmark"><span class="wordmark-dot"></span><span class="wordmark-name">Breezy<br>Brew</span><span class="wordmark-tag">Caribbean Beer</span></div>
  <div class="label-cans">
    <h2>So, why do we use can's?</h2>
    <p>Can's eliminate potential light damage, reduce the risk of oxidation are lighter and chill quicker. Can be enjoyed on beaches and make for great recycling and table art. Plus they are the most recycled and eco-friendly material we can use. Breezy!</p>
  </div>
  <p class="label-alc">Alcohol (ALC) ______% by volume (VOL)<span>Recyclable</span></p>
  <div class="label-pattern bottom" role="img" aria-label="Maroon paisley wave ornament border"></div>
</section>

</body>
</html>
```